Local Motorsports Photography Business Card Design

Looking for a Logo and Business Card design for my father who is a local photographer based in Perth operating under the business name "KLV Photography". Specializing in Motorsports (Torque Racers/Gridcycles/Vorlen Rally) and events photography.
Would like it to look professional, while still maintaining a local/personal feel. Color\Design of the Logo and Card are open to your own interpretation, but should limit the color scheme to around 2-3 colors.
Design should be a logo one side and contact details on the rear. The website currently is very simple and a generic template and should not be used as a basis for design.
Industry/Entity Type
Business
Contact Information for Business Card
Name: Gareth Pindle
Website: www.klvphotography-example.com.au
Email: gareth@klvphotography-example.com.au
Phone: 0455 917 263
Look and feel
Each slider illustrates characteristics of the customer's brand and the style your logo design should communicate.

```html
<!DOCTYPE html>
<html lang="en">
<head>
<meta charset="UTF-8">
<title>KLV Photography – Business Card Back</title>
<link rel="stylesheet" href="https://fonts.googleapis.com/css2?family=Gelasio:wght@400&display=swap">
<style>
  :root {
    --card-centre: #b3b3b3;
    --card-mid: #a0a0a0;
    --card-edge: #7b7b7b;
    --gold: #f1b31c;
    --text-shadow: rgba(40, 40, 40, 0.55);
  }
  html, body {
    margin: 0;
    padding: 0;
    width: 1200px;
    height: 726px;
    overflow: hidden;
    background: var(--card-edge);
  }
  .card-back {
    position: relative;
    width: 1200px;
    height: 726px;
    overflow: hidden;
  }
  .card-texture {
    position: absolute;
    inset: 0;
    background: radial-gradient(ellipse 70% 75% at 50% 38%, var(--card-centre) 0%, var(--card-mid) 45%, var(--card-edge) 100%);
  }
  .contact-details {
    position: absolute;
    left: 0;
    right: 0;
    top: 208px;
    margin: 0;
    text-align: center;
    font-family: "Gelasio", Georgia, serif;
    font-size: 44px;
    line-height: 75px;
    color: var(--gold);
    font-variant-numeric: oldstyle-nums;
    text-shadow: 2px 3px 3px var(--text-shadow);
    font-style: normal;
  }
  .contact-line {
    display: block;
    white-space: nowrap;
  }
</style>
</head>
<body>
  <main class="card-back">
    <div class="card-texture" role="img" aria-label="Soft grey background with a faint low-poly triangle texture"></div>
    <address class="contact-details">
      <span class="contact-line contact-name">Name : Gareth Pindle</span>
      <span class="contact-line contact-website">Website: www.klvphotography-example.com.au</span>
      <span class="contact-line contact-email">Email: gareth@klvphotography-example.com.au</span>
      <span class="contact-line contact-phone">Phone: 0455 917 263</span>
    </address>
  </main>
</body>
</html>
```